You can visit www.corvapeakvitals.com
for your reference.
What we do :
Not just a nutrition plan, not just workout plan
Its a way of life
Balance between eating the right ingredients for your body, knowing what to avoid, taking care of the body (from skin care to muscle care (heart, lungs, organs...) to mental care)

Target Market(s)

Male and Female

Industry/Entity Type

Health And Wellness

Font styles to use
Script

Colors

Designer to choose colors to be used in the design.

Requirements
Must have
• Must focus of Longevity
Nice to have
• Include picture of Maribel in her description.
• You should get inspired from the concept of who we are and what we do for them to reflect this visually in the flyer
• What we do :
• Not just a nutrition plan, not just workout plan
• Its a way of life
• Balance between eating the right ingredients for your body, knowing what to avoid, taking care of the body (from skin care to muscle care (heart, lungs, organs...) to mental care)
Should not have
• Don't include the name Corvapeak Vitals and the Logo as well as the website just put VITALS. kindly use the pictures on the website and the girl doesn’t need to be blonde pick more Brunette, Arabic since we are promoting Dubai. Thank you

```html
<!DOCTYPE html>
<html lang="en">
<head>
<meta charset="utf-8">
<title>VITALS – The Science of Longevity</title>
<link href="https://fonts.googleapis.com/css2?family=Source+Sans+3:ital,wght@0,400;0,600;1,400&family=Merriweather:wght@400&family=Dancing+Script:wght@700&display=swap" rel="stylesheet">
<style>
  :root{
    --navy:#2b3081;
    --navy-soft:#3a3f93;
    --green:#7ab83f;
    --grey:#d9dadd;
    --white:#ffffff;
    --page:#ececec;
    --sky-light:#f6efe2;
    --sky-warm:#e8c98d;
    --lake-light:#e9eef4;
    --lake-blue:#8fa9c6;
  }
  *{margin:0;padding:0;box-sizing:border-box}
  html,body{width:1200px;height:752px;overflow:hidden;background:var(--page)}
  body{position:relative;font-family:"Source Sans 3",Arial,sans-serif;color:var(--navy)}

  .flyer{position:absolute;top:54px;width:490px;height:634px;background:var(--white);overflow:hidden;box-shadow:0 2px 6px rgba(0,0,0,.18)}
  .flyer--front{left:62px}
  .flyer--back{left:608px}
  .flyer__art{position:absolute;inset:0}

  .brand{position:absolute;left:18px;top:30px;display:flex;align-items:center;gap:9px}
  .brand__dot{width:26px;height:26px;border-radius:50%;background:var(--navy)}
  .brand__name{font-size:22px;font-weight:600;color:var(--navy);letter-spacing:3px}

  .event__title{position:absolute;left:15px;top:95px;font-size:18px;font-weight:400;letter-spacing:.2px}
  .event__date{position:absolute;left:15px;top:120px;font-family:"Merriweather",Georgia,serif;font-size:13px;color:#4a4a5a}
  .event__rule{position:absolute;left:15px;top:146px;width:124px;height:3px;background:var(--green)}

  .questions{position:absolute;left:15px;top:170px;width:262px;list-style:none}
  .questions li{position:relative;padding-left:16px;font-size:12px;line-height:14px;margin-bottom:9px;color:var(--navy)}
  .questions li::before{content:"";position:absolute;left:0;top:3px;width:9px;height:9px;border:1.3px solid var(--green);border-radius:50%}

  .tagline{position:absolute;left:20px;top:290px;width:250px;text-align:center;font-family:"Dancing Script",cursive;font-size:16px;line-height:21px;color:var(--navy)}

  .section-head{position:absolute;color:var(--green);text-transform:uppercase;font-weight:400}
  .front-head{left:13px;top:414px;font-size:13.5px;line-height:18px}
  .hearts{position:absolute;list-style:none;color:var(--white)}
  .hearts li{position:relative;padding-left:15px}
  .hearts li::before{content:"\2665";position:absolute;left:0;top:0;color:var(--green)}
  .front-list{left:14px;top:455px;width:250px;font-size:10.5px;line-height:15.2px}

  .services{position:absolute;left:311px;top:420px;width:170px}
  .services__title{font-size:17px;color:var(--white);font-weight:400;margin-bottom:6px}
  .services__title span{color:var(--green)}
  .service{display:flex;align-items:center;gap:12px;height:35.5px}
  .service__icon{width:31px;height:31px;border:1.5px solid var(--white);border-radius:50%;display:flex;align-items:center;justify-content:center;flex:none}
  .service__icon i{width:13px;height:13px;border-radius:50%;background:var(--green)}
  .service__label{font-size:9.5px;line-height:11px;color:var(--white);text-transform:uppercase}

  .bio{position:absolute;left:15px;top:86px;width:228px;font-size:10px;line-height:12.8px;color:var(--navy)}
  .bio p+p{margin-top:12px}

  .back-head{left:15px;top:342px;font-size:12px;line-height:17px}
  .back-list{left:15px;top:380px;width:250px;font-size:10px;line-height:11.5px}
  .back-list li{margin-bottom:8.3px}
  .mission{position:absolute;left:15px;top:582px;width:230px;font-size:8.6px;line-height:11.2px;font-style:italic;color:var(--green)}

  .reviews{position:absolute;right:14px;top:342px;width:190px;text-align:right;color:var(--white);font-style:italic;font-size:8.8px;line-height:11.2px}
  .review{margin-bottom:17px}
  .review__mark{color:var(--green);font-style:normal;font-weight:600;font-size:22px;line-height:8px;vertical-align:-7px;margin-right:3px}
</style>
</head>
<body>

<section class="flyer flyer--front">
  <svg class="flyer__art" viewBox="0 0 490 634" preserveAspectRatio="none">
    <defs>
      <linearGradient id="frontPhoto" x1="0" y1="0" x2="1" y2="0.4">
        <stop offset="0" stop-color="#ffffff"/>
        <stop offset=".35" stop-color="var(--sky-light)"/>
        <stop offset=".7" stop-color="var(--sky-warm)"/>
        <stop offset="1" stop-color="#b9a77a"/>
      </linearGradient>
    </defs>
    <rect role="img" aria-label="Photo of a smiling brunette woman in a sunny field" x="0" y="0" width="490" height="420" fill="url(#frontPhoto)"/>
    <path d="M0,300 Q150,395 330,388 Q420,384 490,360 L490,372 Q420,394 330,398 Q150,404 0,316 Z" fill="var(--green)"/>
    <path d="M0,316 Q150,404 330,398 Q420,394 490,372 L490,634 L0,634 Z" fill="var(--navy)"/>
    <path d="M280,420 Q330,300 490,236 L490,420 Z" fill="var(--navy-soft)" opacity=".75"/>
    <path d="M0,572 Q110,555 200,592 Q255,620 298,634 L0,634 Z" fill="var(--grey)"/>
  </svg>

  <div class="brand"><span class="brand__dot"></span><span class="brand__name">VITALS</span></div>

  <h1 class="event__title">THE SCIENCE OF LONGEVITY</h1>
  <p class="event__date">Dubai, November 8-10, 2019</p>
  <div class="event__rule"></div>

  <ul class="questions">
    <li>Are you overwhelmed and exhausted and feel like there’s no time left for YOU?</li>
    <li>Are you struggling with Chronic Illness, Mood Swings, Bloating, and Hormone Imbalance?</li>
    <li>Have you gained weight due to stress-eating and ready take it off?</li>
  </ul>

  <p class="tagline">Transform Your Lifestyle By Changing<br>The Way You Live</p>

  <h2 class="section-head front-head">Radiate longevity and feel<br>the best version of yourself!</h2>
  <ul class="hearts front-list">
    <li>Heal your gut</li>
    <li>Balance your Hormone</li>
    <li>Feel energetic</li>
    <li>Look &amp; feel better than ever</li>
    <li>Radiate and glow naturally</li>
    <li>Improve nutrition through custom meal plans and counseling for pure vitality and longevity</li>
  </ul>

  <div class="services">
    <h2 class="services__title">OUR <span>SERVICES</span></h2>
    <div class="service"><span class="service__icon"><i></i></span><span class="service__label">Weight loss<br>counseling</span></div>
    <div class="service"><span class="service__icon"><i></i></span><span class="service__label">Functional nutrition<br>education</span></div>
    <div class="service"><span class="service__icon"><i></i></span><span class="service__label">Food allergy<br>management</span></div>
    <div class="service"><span class="service__icon"><i></i></span><span class="service__label">Gut health</span></div>
    <div class="service"><span class="service__icon"><i></i></span><span class="service__label">Balancing<br>hormone</span></div>
  </div>
</section>

<section class="flyer flyer--back">
  <svg class="flyer__art" viewBox="0 0 490 634" preserveAspectRatio="none">
    <defs>
      <linearGradient id="backPhoto" x1="0" y1="0" x2="1" y2="0">
        <stop offset="0" stop-color="#ffffff"/>
        <stop offset=".42" stop-color="#ffffff"/>
        <stop offset=".6" stop-color="var(--lake-light)"/>
        <stop offset="1" stop-color="var(--lake-blue)"/>
      </linearGradient>
    </defs>
    <rect role="img" aria-label="Photo of Maribel meditating on a wooden dock by a lake" x="0" y="0" width="490" height="330" fill="url(#backPhoto)"/>
    <path d="M0,222 Q130,318 320,315 Q420,312 490,290 L490,300 Q420,322 320,326 Q130,330 0,240 Z" fill="var(--green)"/>
    <path d="M0,240 Q130,330 320,326 Q420,322 490,300 L490,634 L0,634 Z" fill="var(--navy)"/>
    <path d="M270,634 Q300,400 490,300 L490,634 Z" fill="var(--navy-soft)" opacity=".8"/>
    <path d="M490,572 Q380,555 310,590 Q265,615 195,634 L490,634 Z" fill="var(--grey)"/>
  </svg>

  <div class="brand"><span class="brand__dot"></span><span class="brand__name">VITALS</span></div>

  <div class="bio">
    <p>Maribel Haddon aboard certified, Transformational Wellness and Nutrition Expert, Member of the Guild of Root-Cause Medicine and of the Global Wellness Coaching Alliance (GWCA) uses functional medicine, to help you find the answers to the root cause of disease instead of just treating symptoms.</p>
    <p>Individualized health and wellness programs for pure vitality and longevity.<br>Pushing science and health forward.</p>
  </div>

  <h2 class="section-head back-head">Functional nutrition education is<br>one of the keys to a happier, healthier life.</h2>
  <ul class="hearts back-list">
    <li>Personalized meal plans especially done according to your genes</li>
    <li>Individualized health and wellness programs for pure vitality and longevity.</li>
    <li>Achieve your longevity goals and have fun doing it.</li>
    <li>Identify food sensitivities</li>
    <li>Balance your hormone</li>
    <li>Improve nutrition through meal plans</li>
    <li>Counseling</li>
    <li>Lose weight</li>
  </ul>

  <p class="mission">Through this course, my purpose is to inspire you and encourage you to be the best version of yourself. Performing up to your full potential and access a greater level of your life.</p>

  <div class="reviews">
    <p class="review"><span class="review__mark">&ldquo;</span>I have more confidence! I struggled to lose weight and feel confident for years until I found the Renewal Reset Program which helped guide my lose 19.5 lbs!” – Lina</p>
    <p class="review"><span class="review__mark">&ldquo;</span>My doctors told me that nutrition did not matter, I knew that was wrong. Now I feel amazing and hopeful again! I’ve reversed leaky Gut, ulcerative colitis, pain, fatigue, depression, and anxiety.”–Omar</p>
    <p class="review"><span class="review__mark">&ldquo;</span>After struggling with my health for many years, I finally found some answers to my health challenges. Going through the program, I lost 35 pounds, regained my confidence and rekindled my marriage.” – Rania</p>
  </div>
</section>

</body>
</html>
```